Private lender of mortgages and rent to own housing

need a website that reflects real estate especially mortgage lending and rent to own houses..
Sections as follows
Home About Types of mortgages Rent to own Contact us
Target Market(s)
consumers who require non traditonal mortgages
Industry/Entity Type
Mortgage
Coding
Coded - Design and coding required
Number of Pages Required
4 page
Font styles to use
Sans Serif
Colors
Designer to choose colors to be used in the design.
Requirements
Must have
- background pictures on pages. with nice picture on homepage of houses or a community
Nice to have
- contact us form i supplied a ink to

```html
<!DOCTYPE html>
<html lang="en">
<head>
<meta charset="utf-8">
<title>Harbourline Home Lending</title>
<link rel="stylesheet" href="https://fonts.googleapis.com/css2?family=Mulish:wght@400;600;700;800&family=Open+Sans:wght@400;600&display=swap">
<style>
  :root {
    --navy: #1f1d5e;
    --indigo: #2e2a7c;
    --indigo-deep: #221f63;
    --ink: #333333;
    --muted: #6b6b6b;
    --line: #cfcfcf;
    --footer: #e4e4e4;
    --white: #ffffff;
    --sky-top: #2a6fd6;
    --sky-low: #7fb2ee;
  }
  * { box-sizing: border-box; margin: 0; padding: 0; }
  html, body { width: 675px; height: 1200px; overflow: hidden; background: var(--white); }
  body { position: relative; font-family: "Open Sans", Arial, sans-serif; color: var(--ink); }

  .site-header { position: absolute; top: 0; left: 0; width: 675px; height: 58px; background: var(--white); }
  .brand { position: absolute; left: 63px; top: 21px; display: flex; align-items: center; gap: 6px;
    font-family: "Mulish", Arial, sans-serif; font-weight: 800; font-size: 10.5px; color: var(--navy); letter-spacing: 0.1px; }
  .brand-dot { width: 12px; height: 12px; border-radius: 50%; background: var(--navy); }
  .main-nav { position: absolute; top: 28px; left: 263px; display: flex; gap: 19px;
    font-family: "Mulish", Arial, sans-serif; font-size: 8.3px; color: var(--muted); letter-spacing: 0.3px; }
  .main-nav .active { color: var(--navy); font-weight: 700; position: relative; }
  .nav-swoosh { position: absolute; left: -8px; top: 11px; }

  .hero { position: absolute; top: 58px; left: 0; width: 675px; height: 307px;
    background: linear-gradient(180deg, var(--sky-top) 0%, var(--sky-low) 45%, #4a4a52 62%, #2d2d33 85%, #5f6b4a 100%); }
  .hero-title { position: absolute; top: 52px; width: 100%; text-align: center; color: var(--white);
    font-family: "Mulish", Arial, sans-serif; font-weight: 600; font-size: 23px; letter-spacing: 0.8px; }
  .hero-sub { position: absolute; top: 82px; width: 100%; text-align: center; color: var(--white);
    font-family: "Mulish", Arial, sans-serif; font-weight: 700; font-size: 16px; letter-spacing: 0.4px; }
  .slider-dots { position: absolute; top: 289px; left: 316px; display: flex; gap: 5px; }
  .slider-dots span { width: 7px; height: 7px; border-radius: 50%; background: var(--white); }
  .slider-dots span:first-child { background: transparent; border: 1px solid var(--white); }

  .about { position: absolute; top: 365px; left: 0; width: 675px; height: 202px; text-align: center; }
  .about h1 { position: absolute; top: 46px; width: 100%; font-family: "Mulish", Arial, sans-serif;
    font-weight: 400; font-size: 16.5px; color: #1a1a1a; letter-spacing: 0.3px; }
  .about-copy { position: absolute; top: 81px; left: 105px; width: 465px; font-size: 7px; line-height: 13px; color: var(--muted); }
  .about-copy p + p { margin-top: 7px; }

  .requirements { position: absolute; top: 567px; left: 0; width: 675px; height: 304px;
    background: linear-gradient(135deg, var(--indigo) 0%, var(--indigo-deep) 55%, #2b2878 100%); }
  .requirements-notch { position: absolute; top: 0; left: 0; }
  .req-item { position: absolute; width: 270px; }
  .req-icon { position: absolute; left: 0; top: 0; width: 54px; height: 54px; border: 2px solid var(--white); border-radius: 50%; }
  .req-icon svg { position: absolute; left: 12px; top: 12px; }
  .req-item h3 { position: absolute; left: 63px; top: 0; font-family: "Mulish", Arial, sans-serif; font-weight: 600;
    font-size: 11.5px; color: var(--white); white-space: nowrap; }
  .req-item p { position: absolute; left: 63px; top: 20px; width: 210px; font-size: 6.3px; line-height: 10.3px; color: #e6e6f3; }

  .testimonials { position: absolute; top: 871px; left: 0; width: 675px; height: 252px; }
  .testimonials h2 { position: absolute; top: 48px; width: 100%; text-align: center; font-family: "Mulish", Arial, sans-serif;
    font-weight: 400; font-size: 15.5px; color: var(--navy); letter-spacing: 0.5px; }
  .quote-card { position: absolute; top: 86px; width: 237px; height: 111px; border: 2px solid var(--line); text-align: center; }
  .avatar { position: absolute; top: -25px; left: 95px; width: 46px; height: 46px; border-radius: 50%;
    background: linear-gradient(160deg, #c9b29a, #6a5a4c); border: 2px solid var(--white); }
  .quote-mark { position: absolute; top: 24px; width: 100%; font-family: Georgia, serif; font-size: 26px; font-weight: 700; color: #bdbdbd; line-height: 1; }
  .quote-text { position: absolute; top: 52px; left: 25px; width: 187px; font-size: 7.6px; line-height: 10.5px; color: var(--muted); }
  .quote-author { position: absolute; top: 78px; width: 100%; font-size: 8px; color: var(--ink); }
  .quote-author strong { font-weight: 400; color: #111; }
  .slider-arrow { position: absolute; top: 131px; }

  .site-footer { position: absolute; top: 1123px; left: 0; width: 675px; height: 77px; background: var(--footer); }
  .footer-nav { position: absolute; top: 25px; left: 66px; display: flex; gap: 16px; font-family: "Mulish", Arial, sans-serif;
    font-size: 7.8px; color: #555; letter-spacing: 0.3px; }
  .copyright { position: absolute; top: 44px; left: 66px; font-size: 6.2px; color: #666; }
  .social { position: absolute; top: 20px; left: 516px; display: flex; gap: 5px; }
  .social span { width: 20px; height: 20px; border-radius: 50%; border: 1.5px solid #222; }
</style>
</head>
<body>

<header class="site-header">
  <div class="brand"><span class="brand-dot"></span>HARBOURLINE HOME LENDING</div>
  <nav class="main-nav">
    <span class="active">HOME
      <svg class="nav-swoosh" width="40" height="8" viewBox="0 0 40 8"><path d="M1 6 Q 18 0 39 4" fill="none" stroke="#1f1d5e" stroke-width="1.6"/></svg>
    </span>
    <span>ABOUT</span>
    <span>TYPES OF MORTGAGES</span>
    <span>RENT TO OWN</span>
    <span>CONTACT US</span>
  </nav>
</header>

<section class="hero" role="img" aria-label="Modern two-storey family home with wood and dark cladding under a blue sky">
  <div class="hero-title">RENT TO OWN A HOME</div>
  <div class="hero-sub">WE CAN PUT YOU IN YOUR OWN HOME TODAY</div>
  <div class="slider-dots"><span></span><span></span><span></span><span></span></div>
</section>

<section class="about">
  <h1>ABOUT HARBOURLINE HOME LENDING</h1>
  <div class="about-copy">
    <p>We know life sometimes delivers challenges and it can be hard to get back on track once you have dealt with challenges. Maybe you have been through a divorce, bankruptcy, consumer proposal, loss of job, work place injury, new to the country, self-employed or some credit related challenges that have you behind the eight ball?</p>
    <p>Are these challenges making it difficult to get a mortgage? None of these things has to bind you to a lifetime of renting. Want to start paying yourself first? We focus on rent to own in Simcoe County and our Renting Program is a very viable option for those that can't get a mortgage today but are willing to work towards getting approved in the near future while living in their own home that they select. Homeownership is closer than you think.</p>
  </div>
</section>

<section class="requirements" role="img" aria-label="Group of smiling people seen from above, tinted indigo">
  <svg class="requirements-notch" width="675" height="36" viewBox="0 0 675 36">
    <polygon points="0,0 160,0 338,31 517,0 675,0 675,0 0,0" fill="#ffffff"/>
    <polyline points="160,0 338,31 517,0" fill="none" stroke="#8c88c8" stroke-width="1.5"/>
  </svg>

  <div class="req-item" style="left:67px; top:73px;">
    <div class="req-icon"><svg width="30" height="30" viewBox="0 0 30 30" fill="none" stroke="#fff" stroke-width="1.4"><rect x="3" y="7" width="22" height="14" rx="1" transform="rotate(-15 14 14)"/><rect x="6" y="10" width="22" height="14" rx="1"/><circle cx="17" cy="17" r="4"/></svg></div>
    <h3>Down Payment</h3>
    <p>We require a minimum down payment of $10,000 or 3.5% to 4% of total price of the home (whichever is larger). So a $400,000 will require a bigger down than a $300,000 house. This is 100% credited towards your purchase of the home. Your down payment is required at the time we have the home inspection.</p>
  </div>

  <div class="req-item" style="left:353px; top:73px;">
    <div class="req-icon"><svg width="30" height="30" viewBox="0 0 30 30" fill="none" stroke="#fff" stroke-width="1.4"><circle cx="13" cy="7" r="4"/><circle cx="19" cy="12" r="4"/><path d="M2 20 L9 19 L16 21 L26 17 L27 20 L16 26 L2 25"/></svg></div>
    <h3>Household Income</h3>
    <p>Steady, provable household income that can support the price of the home you would like. A general guideline is minimum of $50,000 annually but this depends on the price of home you wish to purchase.</p>
  </div>

  <div class="req-item" style="left:67px; top:182px;">
    <div class="req-icon"><svg width="30" height="30" viewBox="0 0 30 30" fill="none" stroke="#fff" stroke-width="1.4"><rect x="9" y="2" width="16" height="22"/><rect x="5" y="6" width="16" height="22" fill="#2a2670"/><path d="M13 12 H18 M13 16 H18 M13 20 H18 M9 12 V20"/></svg></div>
    <h3>Credit Report</h3>
    <p>Although your credit won't necessarily disqualify you from our rent to own program, it is important to know where you stand and what will be needed to improve it while you are in the program. We provide support, you provide the "doing". Credit repair is a commitment.</p>
  </div>

  <div class="req-item" style="left:353px; top:182px;">
    <div class="req-icon"><svg width="30" height="30" viewBox="0 0 30 30" fill="none" stroke="#fff" stroke-width="1.4"><path d="M3 14 L15 3 L27 14"/><path d="M6 12 V27 H24 V12"/><rect x="12" y="18" width="6" height="9"/><rect x="9" y="13" width="4" height="3"/><rect x="17" y="13" width="4" height="3"/></svg></div>
    <h3>Selecting a House</h3>
    <p>May not seem like a strong determining factor overall for qualifying for rent to own but it is for us. You should WANT to select your house as this might be the biggest determining success factor. With our program, you should commit the time to working with one of our realtors to find the "right" house. If you don't love the house, it is going to make it harder to succeed.</p>
  </div>
</section>

<section class="testimonials">
  <h2>TESTIMONIALS</h2>
  <svg class="slider-arrow" style="left:69px" width="12" height="22" viewBox="0 0 12 22"><polyline points="10,2 2,11 10,20" fill="none" stroke="#aaa" stroke-width="2"/></svg>

  <article class="quote-card" style="left:96px;">
    <div class="avatar" role="img" aria-label="Portrait of client"></div>
    <div class="quote-mark">&ldquo;</div>
    <p class="quote-text">I felt very vulnerable after my accident, Owen Pryce helped me get through it.</p>
    <p class="quote-author"><strong>Martin Cole</strong> - Car Accident Client</p>
  </article>

  <article class="quote-card" style="left:342px;">
    <div class="avatar" role="img" aria-label="Portrait of client" style="background:linear-gradient(160deg,#d4b3a0,#4a3a36);"></div>
    <div class="quote-mark">&ldquo;</div>
    <p class="quote-text">They made it an easy process, I recommend them to anyone in need of an attorney.</p>
    <p class="quote-author"><strong>Laura Benton</strong> - Truck Crash Client</p>
  </article>

  <svg class="slider-arrow" style="left:589px" width="12" height="22" viewBox="0 0 12 22"><polyline points="2,2 10,11 2,20" fill="none" stroke="#aaa" stroke-width="2"/></svg>
</section>

<footer class="site-footer">
  <nav class="footer-nav">
    <span>HOME</span><span>ABOUT</span><span>TYPES OF MORTGAGES</span><span>RENT TO OWN</span><span>CONTACT US</span>
  </nav>
  <p class="copyright">&copy; 2017 Company Name &nbsp;All right reserved &nbsp;Term of Use</p>
  <div class="social" aria-label="Social links"><span></span><span></span><span></span><span></span></div>
</footer>

</body>
</html>
```